Geschäftspapiere für Hersteller von Werkstattausrüstung
Zielgruppe
Werkstattausrüstung (Hebebühnen, Achsmessgeräte, Wuchtmaschinen etc.) Zielgruppe Kfz Werkstätte

```html
<!DOCTYPE html>
<html lang="fr">
<head>
<meta charset="utf-8">
<title>KELDOR – Briefbogen</title>
<link href="https://fonts.googleapis.com/css2?family=Open+Sans:wght@400;600;800&family=Roboto:wght@300;400;500&display=swap" rel="stylesheet">
<style>
  :root{
    --backdrop:#d9d9d9;
    --paper:#ffffff;
    --green-dark:#17735a;
    --green-lime:#8cc22c;
    --ink:#1e1e1e;
    --muted:#555;
  }
  *{box-sizing:border-box;margin:0;padding:0}
  html,body{width:1200px;height:1086px;overflow:hidden;background:var(--backdrop)}
  body{font-family:"Open Sans",sans-serif;color:var(--ink)}
  .letterhead{
    position:absolute;left:232px;top:22px;width:736px;height:1042px;
    background:var(--paper);box-shadow:0 4px 18px rgba(0,0,0,.18);
    border-top:4px solid var(--green-lime);overflow:hidden;
  }
  .brand{position:absolute;left:62px;top:92px;display:flex;align-items:center;gap:12px}
  .brand-dot{width:26px;height:26px;border-radius:50%;background:var(--green-dark)}
  .brand-name{font-family:"Open Sans",sans-serif;font-weight:600;font-size:28px;color:var(--green-dark);letter-spacing:1px;line-height:1}
  .sender{
    position:absolute;right:52px;top:44px;padding-left:14px;border-left:1px solid var(--green-dark);
    font-family:"Roboto",sans-serif;font-style:normal;font-weight:300;font-size:9.5px;line-height:1.35;color:var(--green-dark);
  }
  .sender strong{font-weight:500}
  .sender .line{display:flex;align-items:center;gap:5px}
  .sender svg{width:9px;height:9px;flex:none}
  .date{position:absolute;right:90px;top:250px;font-size:8.5px;color:var(--muted)}
  .date span{display:inline-block;width:80px;border-bottom:1px dotted var(--muted);margin-left:3px}
  .body{position:absolute;left:110px;top:330px;width:520px;font-size:8.6px;line-height:1.45}
  .body p{margin-bottom:13px}
  .body ul{list-style:none}
  .body li{position:relative;padding-left:10px;margin-bottom:14px}
  .body li::before{content:"•";position:absolute;left:0}
  .body b{font-weight:800}
  .closing{position:absolute;left:130px;top:640px}
  .closing-name{font-family:"Roboto",sans-serif;font-weight:500;font-size:13px;color:var(--green-dark)}
  .signature{margin-top:8px;width:150px;height:60px;background:#f1f1f1}
  .footer{position:absolute;left:0;bottom:0;width:100%}
  .footer-band{
    background:var(--green-dark);color:#fff;height:74px;display:flex;align-items:center;
    padding:0 40px;font-family:"Roboto",sans-serif;font-size:10.5px;line-height:1.4;font-weight:300
  }
  .footer-band .col{flex:1}
  .footer-band .col strong{font-weight:500}
  .footer-band .sep{width:1px;height:26px;background:rgba(255,255,255,.8);margin:0 28px}
  .footer-strip{
    background:var(--green-lime);height:30px;text-align:center;
    font-family:"Roboto",sans-serif;font-size:16px;color:var(--green-dark);line-height:30px;font-weight:400
  }
</style>
</head>
<body>
<main class="letterhead">
  <header>
    <div class="brand">
      <div class="brand-dot"></div>
      <div class="brand-name">KELDOR</div>
    </div>
    <address class="sender">
      <div><strong>KELDOR</strong> GmbH &amp; Co. KG</div>
      <div>Werkhofstraße 14</div>
      <div>64001 Talheim</div>
      <div class="line">
        <svg viewBox="0 0 10 10" aria-hidden="true"><path d="M2 1l2 2-1 1.2c.6 1.2 1.6 2.2 2.8 2.8L7 6l2 2-1.3 1.3C4.5 9 1 5.5.7 2.3z" fill="none" stroke="var(--green-lime)" stroke-width=".9"/></svg>
        06201 / 555 40 0
      </div>
      <div class="line">
        <svg viewBox="0 0 10 10" aria-hidden="true"><rect x=".5" y="2" width="9" height="6" fill="none" stroke="var(--green-lime)" stroke-width=".9"/><path d="M.5 2l4.5 3.5L9.5 2" fill="none" stroke="var(--green-lime)" stroke-width=".9"/></svg>
        info@keldor-technik.de
      </div>
    </address>
  </header>

  <div class="date">Date<span></span></div>

  <section class="body">
    <p>Bonjour Monsieur</p>
    <ul>
      <li>A l’approbation de cette commande la société <b>ATELIER NORD</b> se soumet et s’engage à exécuter l’ensemble d’agencement objet de cet écrit dans les délais et dans les normes de sécurité et garantie appliqués par la loi en vigueur.</li>
      <li>Toutes modification apporter a l’une des clauses de cette présente commande doit faire objets d’un avenant signer par les deux partie maximum 24h à partir de la date de la confirmation.</li>
      <li>La marchandise objet de cette commande ainsi que les plans techniques et autres restent les propriétés exclusives de la société atelier nord jusqu’au paiement intégrale de la facture ainsi qu’au règlement de toutes autres prestations impliqués directement ou indirectement dans cette commande.</li>
      <li>Le délai de livraison et installation commerce à courir à partir de la date ou le client invite la société <b>ATELIER NORD</b> à passer les mesures et relevé des cotés finies sur place.</li>
      <li>Le délai de livraison et installation doit être impérativement respecté par les deux parties et dans le cas où une prolongation dans les délais est souhaiter par le client pour quelques raison que ce soit (arrêt momentanée du chantier : retard imprévu dans les travaux …etc.) il doit expressément aviser nos services compétent pour convenir une ultérieure date de livraison qui n’excédé en aucune cas 90 jours dépassant ce délai la société <b>ATELIER NORD</b> est libre de considérer l’annulation pure et simple de la vente aussi que le client n’aura aucun recourt à récupérer les sommes perçus comme avances ainsi qu’il est invité à régler l’intégralité de sommes restantes des différentes prestations objet de cette commande.</li>
    </ul>
  </section>

  <div class="closing">
    <div class="closing-name">Your Name HERE</div>
    <div class="signature" role="img" aria-label="Handschriftliche Unterschrift"></div>
  </div>

  <footer class="footer">
    <div class="footer-band">
      <div class="col"><strong>Bankverbindung:</strong><br>Ihr Name der Bank hier</div>
      <div class="sep"></div>
      <div class="col"><strong>BIC:</strong> XXXXXX56XXX<br><strong>IBAN:</strong> DE69 3458 4764 864 XXXXX XX</div>
      <div class="sep"></div>
      <div class="col"><strong>Steuer Nummer:</strong> 652 486 XXXXX<br><strong>Umsatzsteuer-ID-Nr:</strong> DE 652347XXX</div>
    </div>
    <div class="footer-strip">www.keldor-technik.de</div>
  </footer>
</main>
</body>
</html>
```